Corvalen Coffee Bag for Retail Desing

.Our name and logo represent two things about the identity of our brand Turquoise Blue which is the color of the Honduras flag and the Guacamaya Bird (Ara Macao) national bird of Honduras we want that our logo and our packing reflects the peace that you can find by brewing your coffee and also the quality of our product which comes from one of the greatest coffee beans in the world.

We are looking for a design for our coffee bag there are some elements that we need to incorporate into the bag and we are providing you with a word document with guidelines to do it

Target Market(s)

Specialty coffee consumers is the United States

Industry/Entity Type

Product

Logo Text

CORVALEN COFFEE

Colors

Designer to choose colors to be used in the design.

Requirements
Must have
• Logo / Name of Brand
• Please Check Guidelines on Word Document
Nice to have
• The bag will be sent to print and all details are customizable feel free to be creative
Should not have

```html
<!DOCTYPE html>
<html lang="en">
<head>
<meta charset="utf-8">
<title>Corvalen Coffee – Bag Layout</title>
<link href="https://fonts.googleapis.com/css2?family=Montserrat:wght@500;700;800&family=Oswald:wght@400;500&display=swap" rel="stylesheet">
<style>
  :root{
    --paper:#ffffff;
    --feather-red:#e2574b;
    --feather-deep:#0f3f5e;
    --feather-mid:#1a6f96;
    --feather-light:#2a8dba;
    --ink-white:#ffffff;
    --ink-soft:#c9d3da;
    --guide:#4fb3e0;
    --accent-red:#e8453c;
    --accent-lime:#d4dc2a;
    --label-grey:#c4c5c9;
    --note-bg:#ececec;
  }
  *{margin:0;padding:0;box-sizing:border-box}
  html,body{width:1200px;height:950px;overflow:hidden;background:var(--paper)}
  .canvas{position:relative;width:1200px;height:950px;font-family:"Montserrat",sans-serif;color:var(--ink-white)}

  .dieline{position:absolute;left:46px;top:72px;width:908px;height:802px;overflow:hidden}
  .feather-art{position:absolute;inset:0;
    background:
      linear-gradient(180deg,var(--feather-red) 0%,#a8404a 12%,var(--feather-deep) 26%,var(--feather-mid) 40%,var(--feather-light) 52%,var(--feather-deep) 64%,var(--feather-mid) 78%,var(--feather-deep) 100%);}
  .guide{position:absolute;top:14px;bottom:14px;width:1px;background:var(--guide);opacity:.8}
  .guide-h{position:absolute;left:22px;right:22px;height:1px;background:var(--guide);opacity:.8}

  .copy{position:absolute;text-align:center;font-weight:800;font-size:7.4px;line-height:9.2px;letter-spacing:.15px;text-transform:uppercase}
  .fine{position:absolute;text-align:center;font-family:"Oswald",sans-serif;font-weight:400;font-size:8px;line-height:11px;color:var(--ink-soft);text-transform:uppercase}

  .panel-frame{position:absolute;border:1.6px solid var(--ink-white)}
  .art-slot{position:absolute;border-radius:4px}

  .brand-kicker{position:absolute;left:0;width:908px;text-align:center;font-weight:700;font-size:6.5px;letter-spacing:.3px}
  .brand-name{position:absolute;text-align:center;font-weight:500;font-size:24px;line-height:25px;letter-spacing:.5px}
  .roast{position:absolute;left:0;width:908px;text-align:center;font-weight:700;font-size:14.5px;letter-spacing:.6px}
  .roast-note{position:absolute;left:0;width:908px;text-align:center;font-weight:700;font-size:6.8px;line-height:13.6px;letter-spacing:.3px}

  .best-before{position:absolute;left:767px;top:566px;width:88px;height:38px;background:var(--label-grey);color:#1b2330;font-family:"Oswald",sans-serif;font-size:7.5px;font-weight:500;text-align:center;padding-top:6px}

  .detail{position:absolute;left:985px;width:178px;height:178px;overflow:hidden}
  .map-note{position:absolute;left:13px;top:60px;width:154px;height:68px;background:var(--note-bg);color:var(--accent-red);font-family:"Montserrat",sans-serif;font-weight:500;font-size:11.5px;line-height:16px;text-align:center;padding-top:10px}
</style>
</head>
<body>
<div class="canvas">

  <section class="dieline">
    <div class="feather-art" role="img" aria-label="Illustrated macaw feather pattern, red feathers at top fading into turquoise and deep blue rows"></div>

    <div class="guide" style="left:56px"></div>
    <div class="guide" style="left:181px"></div>
    <div class="guide" style="left:322px"></div>
    <div class="guide" style="left:604px"></div>
    <div class="guide" style="left:744px"></div>
    <div class="guide" style="left:866px"></div>
    <div class="guide-h" style="top:14px"></div>
    <div class="guide-h" style="top:786px"></div>

    <!-- Side panel: story -->
    <p class="copy" style="left:42px;width:152px;top:278px">This special batch<br>has been harvested<br>in Las Nubes Farm,<br>located at an<br>altitude of 1350<br>meters above sea<br>level, delivering<br>you a delicious,<br>full-bodied aroma<br>and rich taste.<br>We love great<br>coffee and great<br>people like you.<br><br>Ingredients:<br>100% Arabica<br>coffee</p>
    <p class="fine" style="left:42px;width:152px;top:554px">Distributed by:<br>Corvalen Coffee,<br>City, State, Zip Code<br>Packed in Honduras by:<br>Verapaz Export S. de R.L.</p>

    <!-- Origin panel -->
    <div class="panel-frame" style="left:194px;top:198px;width:117px;height:424px"></div>
    <div class="art-slot" role="img" aria-label="White line drawing of an olive branch" style="left:208px;top:178px;width:58px;height:52px;background:linear-gradient(135deg,rgba(255,255,255,.35),rgba(255,255,255,.1))"></div>
    <p class="copy" style="left:194px;width:117px;top:254px">Honduras is<br>a country that<br>has cultivated<br>arabica-specialty<br>coffee for over<br>200 years. This<br>historic tradition<br>of coffee has been<br>maintained and<br>developed by<br>small farmers.<br>Most of the coffee<br>production is<br>exported to<br>Europe. Today,<br>Honduras has<br>established its<br>position as one<br>of the top ten<br>worldwide coffee<br>producers.</p>
    <div class="art-slot" role="img" aria-label="White outline map of Honduras with a red dot marking the farm region" style="left:184px;top:492px;width:140px;height:82px;background:linear-gradient(180deg,rgba(255,255,255,.28),rgba(255,255,255,.12))"></div>

    <!-- Front panel -->
    <div class="art-slot" role="img" aria-label="Scarlet macaw perched on a leafy branch, red, lime and white line illustration" style="left:514px;top:224px;width:68px;height:124px;background:linear-gradient(180deg,var(--accent-red) 0%,var(--accent-red) 45%,var(--accent-lime) 60%,var(--accent-red) 100%);opacity:.85"></div>
    <p class="brand-kicker" style="top:311px">100% HONDURAS COFFEE</p>
    <p class="brand-name" style="left:0;width:908px;top:330px">CORVALEN<br>COFFEE</p>
    <p class="brand-kicker" style="top:390px">SINGLE ORIGIN</p>
    <p class="roast" style="top:476px">MEDIUM DARK</p>
    <p class="roast-note" style="top:502px">SMALL BATCH ROASTED<br>FARM DIRECT TRADE</p>
    <p class="fine" style="left:0;width:908px;top:591px;font-size:9.5px">NET WEIGHT 16OZ (1LB 16OZ) • 453G</p>

    <!-- Brewing panel -->
    <div class="panel-frame" style="left:615px;top:202px;width:118px;height:420px"></div>
    <div class="art-slot" role="img" aria-label="White line drawing of a leafy branch" style="left:600px;top:196px;width:94px;height:62px;background:linear-gradient(135deg,rgba(255,255,255,.35),rgba(255,255,255,.1))"></div>
    <p class="copy" style="left:615px;width:118px;top:282px">Coffee is personal<br>so adjust these<br>measurements<br>to your liking.<br><br>We suggest: 1<br>tablespoon for each<br>5 oz of cold filtered<br>water.1 TBS =15 GR<br><br>For more information<br>about how to brew a<br>good cup of coffee<br>visit our website:<br>corvalencoffee.com</p>
    <div class="art-slot" role="img" aria-label="Small scarlet macaw on a branch" style="left:698px;top:452px;width:40px;height:98px;background:linear-gradient(180deg,var(--accent-red) 0%,var(--accent-lime) 40%,var(--accent-red) 100%);opacity:.85"></div>
    <p class="brand-name" style="left:615px;width:100px;top:504px;font-size:15px;line-height:16px">CORVALEN<br>COFFEE</p>

    <!-- Company panel -->
    <p class="copy" style="left:756px;width:108px;top:286px">Corvalen Coffee<br>is an American<br>company that has<br>partnered with<br>local farmers<br>in Honduras<br>to provide a<br>single-origin<br>coffee. We pick,<br>toast, and pack<br>it ourselves to<br>serve you one of<br>the best coffees<br>in the world.</p>
    <p class="fine" style="left:746px;width:128px;top:530px;font-size:7.6px">Contact us:<br>hello@corvalencoffee.com<br>www.corvalencoffee.com</p>
    <div class="best-before">BEST BEFORE</div>
  </section>

  <!-- Detail views -->
  <div class="detail" style="top:161px" role="img" aria-label="Close-up of the turquoise feather texture" >
    <div style="position:absolute;inset:0;background:linear-gradient(160deg,#123e5c 0%,#2a8dba 45%,#14496b 100%)"></div>
  </div>
  <div class="detail" style="top:366px" role="img" aria-label="Close-up of the macaw illustration in red, lime and white lines">
    <div style="position:absolute;inset:0;background:linear-gradient(160deg,#1a6f96 0%,#e8453c 50%,#d4dc2a 75%,#14496b 100%)"></div>
  </div>
  <div class="detail" style="top:568px">
    <div role="img" aria-label="Close-up of the Honduras outline map with red location dot" style="position:absolute;inset:0;background:linear-gradient(180deg,#14496b 0%,#1e6f96 100%)"></div>
    <p class="map-note">MAP TO BE UPDATED<br>IN FINALISATION<br>IF CONCEPT IS CHOOSEN</p>
  </div>

</div>
</body>
</html>
```